Packaging design for a reclosable bag for our product

We have a logo, and we need to put it on packaging for our product and while we want the look to be simple, we want it to follow good design principles and also contain spaces for other product descriptions.

There will be 5 sizes at launch so I'd like 5 variations, one for each size.

I've included a few mockups of the type of bag that I made but they are all just rough ideas that I had.

I want the brand to look scientific and methodical and even a bit quirky, as in "wow this is a serious product but also a bit unusual."

```html
<!DOCTYPE html>
<html lang="en">
<head>
<meta charset="utf-8">
<title>KR4 Bias Lighting – Extra Large 5 meters</title>
<link rel="stylesheet" href="https://fonts.googleapis.com/css2?family=Jost:wght@400;700&display=swap">
<style>
  :root {
    --pack-black: #000000;
    --ink-white: #ffffff;
  }
  html, body {
    margin: 0;
    padding: 0;
    width: 960px;
    height: 1200px;
    overflow: hidden;
    background: var(--pack-black);
  }
  .pack-face {
    display: block;
    width: 960px;
    height: 1200px;
    background: var(--pack-black);
  }
  .pack-face text {
    fill: var(--ink-white);
    font-family: "Jost", "Futura", sans-serif;
  }
  .size-label { font-size: 43px; font-weight: 400; }
  .size-length { font-size: 67px; font-weight: 700; }
  .brand-name { font-size: 400px; font-weight: 700; }
  .product-line { font-size: 92px; font-weight: 700; }
  .spec-line { font-size: 42px; font-weight: 400; }
</style>
</head>
<body>
<svg class="pack-face" viewBox="0 0 960 1200" xmlns="http://www.w3.org/2000/svg">
  <text class="size-label" x="763" y="375" text-anchor="end">Extra Large</text>
  <text class="size-length" x="763" y="438" text-anchor="end">5 meters</text>
  <text class="brand-name" x="196" y="739" textLength="566" lengthAdjust="spacingAndGlyphs">KR4</text>
  <text class="product-line" x="194" y="822" textLength="506" lengthAdjust="spacingAndGlyphs">Bias Lighting</text>
  <text class="spec-line" x="199" y="922">Simulated D65 CRI 90+</text>
  <text class="spec-line" x="199" y="978">6500K White Bias Lighting</text>
</svg>
</body>
</html>
```